Silver Creek Plumbing Business card & letter head design

We need a new business card and letter head for our plumbing company called silver creek plumbing. attached is the companys logo. We provide domestic and commercial plumbing services in regional western Australia. We are after Something simple yet nice to look at and something that fits within the trade industry.

Target Market(s)

trade/building industry

Contact Information for Business Card

Darl Hensby
Manager
0461 238 574
enquiries@scplumbwork.net.au
ABN: 47 381 905 462
PCL: 5187

Domestic & Commercial Plumbing
Tip Truck & Excavator hire

Colors

Designer to choose colors to be used in the design.

```html
<!DOCTYPE html>
<html lang="en">
<head>
<meta charset="utf-8">
<title>Silver Creek Plumbing – Stationery</title>
<link rel="stylesheet" href="https://fonts.googleapis.com/css2?family=Roboto:ital,wght@0,400;0,500;0,700;1,700&display=swap">
<style>
  :root {
    --brand-blue: #0f55a8;
    --flap-blue: #143f8a;
    --ink: #3a3a3a;
    --rule: #b9b9b9;
    --paper: #ffffff;
    --faint: #eeeff1;
    --stage: #8c8c8c;
  }
  * { box-sizing: border-box; margin: 0; padding: 0; }
  html, body { width: 1200px; height: 840px; overflow: hidden; }
  body {
    background: var(--stage);
    font-family: "Roboto", Arial, sans-serif;
    color: var(--ink);
    position: relative;
  }
  .sheet {
    position: absolute;
    background: var(--paper);
    box-shadow: 0 3px 8px rgba(0,0,0,0.3);
    overflow: hidden;
  }
  .brand-name {
    font-family: "Roboto", Arial, sans-serif;
    font-weight: 700;
    color: var(--brand-blue);
    white-space: nowrap;
    letter-spacing: 0.01em;
  }
  .faint-mark {
    position: absolute;
    background: var(--faint);
  }

  /* Letterhead */
  .letterhead { left: 34px; top: 85px; width: 509px; height: 703px; }
  .letterhead .brand-name {
    position: absolute; top: 34px; left: 0; width: 100%;
    text-align: center; font-size: 17px;
  }
  .letterhead .faint-mark { left: 67px; top: 251px; width: 378px; height: 153px; }
  .letterhead .service-band {
    position: absolute; left: 0; top: 641px; width: 100%; height: 21px;
    background: var(--brand-blue); color: #fff;
    font-size: 9.5px; font-weight: 500; text-align: center; line-height: 21px;
  }
  .letterhead .contact {
    position: absolute; left: 0; top: 667px; width: 100%;
    text-align: center; font-size: 7.6px; line-height: 10px; color: #4a4a4a;
  }
  .icon { display: inline-block; vertical-align: -1px; }

  /* Business card front */
  .card-front { left: 556px; top: 104px; width: 230px; height: 140px; background: var(--brand-blue); }
  .card-front .faint-band {
    position: absolute; left: 0; top: 49px; width: 100%; height: 45px; background: #eceef2;
  }
  .card-front .brand-name {
    position: absolute; left: 0; top: 102px; width: 100%;
    text-align: center; color: #fff; font-size: 15px;
  }

  /* Business card back */
  .card-back { left: 800px; top: 105px; width: 230px; height: 139px; }
  .card-back .person {
    position: absolute; right: 16px; top: 11px; text-align: right; line-height: 1;
  }
  .person-name { color: var(--brand-blue); font-weight: 700; font-size: 7.6px; }
  .person-role { font-size: 4.6px; color: #555; margin-top: 1px; }
  .person-phone { font-size: 6.4px; font-weight: 700; margin-top: 2px; }
  .card-back .brand-name { position: absolute; left: 11px; top: 46px; font-size: 11px; }
  .card-back .rule { position: absolute; left: 0; right: 0; top: 61px; border-top: 1px solid var(--rule); }
  .services { line-height: 1.15; }
  .services .primary { color: var(--brand-blue); font-weight: 700; }
  .services .secondary { font-weight: 700; color: var(--ink); }
  .card-back .services { position: absolute; left: 11px; top: 68px; font-size: 8.6px; }
  .card-back .contact {
    position: absolute; right: 16px; top: 106px; text-align: right;
    font-size: 5.6px; line-height: 7.4px; color: #444;
  }
  .card-back .edge-bar {
    position: absolute; right: 0; top: 106px; width: 7px; height: 24px; background: var(--brand-blue);
  }

  /* Envelope front */
  .envelope-front { left: 556px; top: 262px; width: 608px; height: 250px; }
  .envelope-front .brand-name { position: absolute; left: 14px; top: 38px; font-size: 10px; }
  .envelope-front .rule { position: absolute; left: 0; right: 0; top: 53px; border-top: 1px solid var(--rule); }
  .envelope-front .services { position: absolute; left: 14px; top: 194px; font-size: 6.3px; }
  .envelope-front .services-rule {
    position: absolute; left: 14px; top: 213px; width: 127px; border-top: 1px solid #777;
  }
  .envelope-front .contact {
    position: absolute; left: 14px; top: 217px; font-size: 5.2px; line-height: 7.6px; color: #444;
  }
  .envelope-front .faint-mark { left: 361px; top: 151px; width: 247px; height: 99px; }

  /* Envelope back */
  .envelope-back { left: 556px; top: 522px; width: 607px; height: 250px; }
  .envelope-back svg { position: absolute; left: 0; top: 0; }
</style>
</head>
<body>

  <section class="sheet letterhead" aria-label="Letterhead">
    <div class="brand-name">Silver Creek Plumbing</div>
    <div class="faint-mark" role="img" aria-label="Faint brand name watermark area"></div>
    <div class="service-band">Domestic &amp; Commercial Plumbing | Tip Truck &amp; Excavator <i>hire</i></div>
    <div class="contact">
      <svg class="icon" width="8" height="6" viewBox="0 0 8 6" aria-hidden="true"><rect x="0.5" y="0.5" width="7" height="5" fill="none" stroke="#0f55a8" stroke-width="0.8"/><path d="M0.5 0.5 L4 3.3 L7.5 0.5" fill="none" stroke="#0f55a8" stroke-width="0.8"/></svg>
      enquiries@scplumbwork.net.au
      <svg class="icon" width="5" height="8" viewBox="0 0 5 8" aria-hidden="true"><rect x="0.5" y="0.5" width="4" height="7" rx="0.8" fill="none" stroke="#0f55a8" stroke-width="0.8"/></svg>
      0461 238 574<br>
      ABN: 47 381 905 462<br>
      PCL: 5187
    </div>
  </section>

  <section class="sheet card-front" aria-label="Business card front">
    <div class="faint-band" role="img" aria-label="Light band for faint brand pattern"></div>
    <div class="brand-name">Silver Creek Plumbing</div>
  </section>

  <section class="sheet card-back" aria-label="Business card back">
    <div class="person">
      <div class="person-name">Darl Hensby</div>
      <div class="person-role">Manager</div>
      <div class="person-phone">0461 238 574</div>
    </div>
    <div class="brand-name">Silver Creek Plumbing</div>
    <div class="rule"></div>
    <div class="services">
      <div class="primary">Domestic &amp; Commercial Plumbing</div>
      <div class="secondary">Tip Truck &amp; Excavator <i>hire</i></div>
    </div>
    <div class="contact">
      enquiries@scplumbwork.net.au<br>
      ABN: 47 381 905 462<br>
      PCL: 5187
    </div>
    <div class="edge-bar"></div>
  </section>

  <section class="sheet envelope-front" aria-label="Envelope front">
    <div class="brand-name">Silver Creek Plumbing</div>
    <div class="rule"></div>
    <div class="services">
      <div class="primary">Domestic &amp; Commercial Plumbing</div>
      <div class="primary">Tip Truck &amp; Excavator <i style="color:var(--ink)">hire</i></div>
    </div>
    <div class="services-rule"></div>
    <div class="contact">
      <svg class="icon" width="6" height="5" viewBox="0 0 8 6" aria-hidden="true"><rect x="0.5" y="0.5" width="7" height="5" fill="none" stroke="#0f55a8" stroke-width="0.8"/><path d="M0.5 0.5 L4 3.3 L7.5 0.5" fill="none" stroke="#0f55a8" stroke-width="0.8"/></svg>
      enquiries@scplumbwork.net.au
      <svg class="icon" width="4" height="6" viewBox="0 0 5 8" aria-hidden="true"><rect x="0.5" y="0.5" width="4" height="7" rx="0.8" fill="none" stroke="#0f55a8" stroke-width="0.8"/></svg>
      0461 238 574<br>
      ABN: 47 381 905 462<br>
      PCL: 5187
    </div>
    <div class="faint-mark" role="img" aria-label="Faint brand name watermark area"></div>
  </section>

  <section class="sheet envelope-back" aria-label="Envelope back">
    <svg width="607" height="90" viewBox="0 0 607 90" role="img" aria-label="Envelope flap with blue brand pattern">
      <path d="M0 0 H607 Q598 48 548 51 L303 81 L58 51 Q8 48 0 0 Z" fill="var(--flap-blue)"/>
    </svg>
  </section>

</body>
</html>
```